Webdesign für Unternehmen im Bereich der Prozessautomatisierung und Gebäudeautomation
Zielgruppe
Wir befinden uns derzeit in der Gründungsphase und möchten ein neuer Dienstleister im Bereich der Automatisierung werden. Wir haben uns dazu auf zwei Kernaufgaben spezialisiert:
Prozessautomatisierung und Gebäudeautomation.
Aufgabenstellung
Gesucht wird nur eine Seite für Bereich Prozessautomatisierung. Die weiteren Seiten kommen zu eine späteren Zeitpunkt.
Texte sind leider noch nicht vorhanden. Sie können Fülltext verwenden oder sich selbst etwas überlegen.
Für das Design eventuell relevante Punkte sind die folgenden:
Die Seite soll locker gestaltet sein. Die betrachtende Person darf nicht vom Text erschlagen werden.
Ziel mit unserer Applikation:
… Kosten- und Zeitersparnis beim Kunden zu erzielen!
… Fehler zu reduzieren und ganz zu vermeiden!

```html
<!DOCTYPE html>
<html lang="de">
<head>
<meta charset="utf-8">
<title>Norvatec – ERP-Lösung</title>
<link rel="stylesheet" href="https://fonts.googleapis.com/css2?family=Exo+2:wght@400;700&family=Roboto:wght@700&display=swap">
<style>
  :root {
    --navy: #0c1150;
    --navy-deep: #0a0f46;
    --teal-glow: #0a5f95;
    --accent: #00c9d3;
    --white: #ffffff;
    --text-soft: #d6dcf0;
    --photo-dark: #242c44;
    --photo-mid: #4a5268;
    --photo-light: #6f6a70;
  }
  * { margin: 0; padding: 0; box-sizing: border-box; }
  html, body { width: 1200px; height: 684px; overflow: hidden; background: var(--navy); }
  .hero {
    position: relative;
    width: 1200px;
    height: 684px;
    overflow: hidden;
    background: var(--navy);
    font-family: "Exo 2", sans-serif;
    color: var(--white);
  }
  .hero-visual { position: absolute; inset: 0; }
  .site-header {
    position: absolute;
    top: 0; left: 0;
    width: 1200px;
    height: 92px;
    border-bottom: 1px solid rgba(255,255,255,0.12);
  }
  .brand {
    position: absolute;
    left: 40px; top: 24px;
    display: flex;
    align-items: center;
    gap: 22px;
  }
  .brand-mark {
    width: 44px; height: 44px;
    background: var(--white);
    border-radius: 6px;
  }
  .brand-name {
    font-family: "Exo 2", sans-serif;
    font-weight: 700;
    font-size: 38px;
    letter-spacing: 1px;
    line-height: 1;
    color: var(--white);
  }
  .main-nav {
    position: absolute;
    top: 44px;
    right: 46px;
    display: flex;
    gap: 30px;
    font-family: Arial, Helvetica, sans-serif;
    font-size: 18.5px;
    color: var(--white);
  }
  .main-nav a { color: inherit; text-decoration: none; }
  .hero-content {
    position: absolute;
    left: 192px;
    top: 282px;
  }
  .hero-title {
    font-weight: 700;
    font-size: 80px;
    line-height: 1;
    letter-spacing: 0.5px;
  }
  .hero-lead {
    margin-top: 24px;
    font-size: 12.8px;
    line-height: 22px;
    color: var(--text-soft);
  }
  .hero-button {
    display: inline-block;
    margin-top: 40px;
    width: 178px;
    height: 42px;
    line-height: 42px;
    text-align: center;
    background: var(--accent);
    border-radius: 2px;
    font-family: "Roboto", sans-serif;
    font-weight: 700;
    font-size: 13.5px;
    color: var(--white);
    text-decoration: none;
  }
</style>
</head>
<body>
<section class="hero">
  <svg class="hero-visual" width="1200" height="684" viewBox="0 0 1200 684">
    <defs>
      <radialGradient id="edgeGlow" cx="380" cy="330" r="300" gradientUnits="userSpaceOnUse">
        <stop offset="0" stop-color="var(--teal-glow)" stop-opacity="0.9"/>
        <stop offset="1" stop-color="var(--navy)" stop-opacity="0"/>
      </radialGradient>
      <linearGradient id="photoTone" x1="0" y1="0" x2="1" y2="1">
        <stop offset="0" stop-color="var(--photo-dark)"/>
        <stop offset="0.55" stop-color="var(--photo-mid)"/>
        <stop offset="1" stop-color="var(--photo-light)"/>
      </linearGradient>
      <linearGradient id="photoShade" x1="0" y1="0" x2="0" y2="1">
        <stop offset="0" stop-color="#0c1150" stop-opacity="0.35"/>
        <stop offset="0.3" stop-color="#0c1150" stop-opacity="0"/>
      </linearGradient>
    </defs>
    <rect width="1200" height="684" fill="var(--navy)"/>
    <path d="M250 0 C 270 220, 350 470, 560 585 L 250 684 L 0 684 L 0 0 Z" fill="url(#edgeGlow)"/>
    <path role="img" aria-label="Foto: Hand tippt auf einer Laptop-Tastatur, daneben Kopfhörerkabel"
          d="M329 0 C 345 210, 420 470, 600 590 C 760 660, 1000 650, 1200 642 L1200 0 Z"
          fill="url(#photoTone)"/>
    <path d="M329 0 C 345 210, 420 470, 600 590 C 760 660, 1000 650, 1200 642 L1200 0 Z"
          fill="url(#photoShade)"/>
  </svg>

  <header class="site-header">
    <div class="brand">
      <span class="brand-mark"></span>
      <span class="brand-name">NORVATEC</span>
    </div>
    <nav class="main-nav">
      <a href="#">Home</a>
      <a href="#">ERP-Applikation</a>
      <a href="#">Gebäudeautomation</a>
      <a href="#">Über uns</a>
      <a href="#">Kontakt</a>
    </nav>
  </header>

  <div class="hero-content">
    <h1 class="hero-title">ERP-Lösung</h1>
    <p class="hero-lead">Die passende ERP-Lösung für jedes Unternehmen<br>Informieren Sie sich jetzt!</p>
    <a class="hero-button" href="#">Erfahren Sie mehr!</a>
  </div>
</section>
</body>
</html>
```